Design for Outdoor Sign/Banner to be used at Markets/Pop Up Events

We are a small boutique nursery based in Warner, Qld specialising in Platycerium species. We propagate, grow and sell the 18 different species of Platycerium. All of our Platyceriums are grown in shade houses on site and are hardened in natural conditions. We would like to see designs that use the colour green. I will attach our Company Logo and also the Stubbie Cooler Design that a designer created through Brief Foundry. Banner size would be approx 2 metres wide, 1 metre high.

```html
<!DOCTYPE html>
<html lang="en">
<head>
<meta charset="utf-8">
<title>Antler Grove – Market Banner</title>
<link href="https://fonts.googleapis.com/css2?family=Bebas+Neue&family=Poppins:ital,wght@1,400&display=swap" rel="stylesheet">
<style>
  :root {
    --green-bright: #0fa35a;
    --green-mid: #0a7a3e;
    --green-deep: #06582a;
    --green-logo: #0b6b1e;
    --yellow: #f5ea2a;
    --white: #ffffff;
    --product-dark: #2a2f2b;
    --product-light: #e9ece4;
    --product-fern: #a9c98c;
  }
  * { margin: 0; padding: 0; box-sizing: border-box; }
  html, body { width: 1200px; height: 710px; overflow: hidden; background: var(--green-deep); }
  .banner {
    position: relative;
    width: 1200px;
    height: 710px;
    overflow: hidden;
    background: linear-gradient(180deg, var(--green-bright) 0%, var(--green-mid) 55%, var(--green-deep) 78%);
    font-family: "Bebas Neue", "Arial Narrow", sans-serif;
    color: var(--white);
  }
  .shelf-top {
    position: absolute; left: 0; top: 550px; width: 1200px; height: 91px;
    background: linear-gradient(180deg, var(--green-mid) 0%, var(--green-bright) 30%, var(--green-bright) 100%);
  }
  .shelf-front {
    position: absolute; left: 0; top: 641px; width: 1200px; height: 69px;
    background: var(--green-deep);
    border-top: 2px solid rgba(255,255,255,0.25);
  }
  .brand-mark {
    position: absolute; left: 55px; top: 93px; width: 185px; height: 242px;
    background: var(--white);
    display: flex; align-items: center; justify-content: center;
    color: var(--green-logo);
    font-size: 60px; line-height: 0.95; text-align: center;
  }
  .headline {
    position: absolute; left: 267px; top: 81px;
    font-weight: 400;
    font-size: 80px; line-height: 87px; letter-spacing: 0.3px;
    text-shadow: 3px 4px 6px rgba(0,0,0,0.3);
    white-space: nowrap;
  }
  .headline .accent { color: var(--yellow); }
  .tagline {
    position: absolute; left: 56px; top: 400px; width: 421px; height: 98px;
    border: 1px solid rgba(255,255,255,0.8);
    padding: 6px 12px;
    font-family: "Poppins", sans-serif; font-style: italic; font-weight: 400;
    font-size: 24px; line-height: 35px;
    white-space: nowrap;
  }
  .social {
    position: absolute; left: 55px; top: 581px;
    display: flex; align-items: center; gap: 13px;
  }
  .social-dot {
    width: 31px; height: 31px;
    border: 3px solid var(--white); border-radius: 8px;
  }
  .social-handle { font-size: 27px; line-height: 31px; letter-spacing: 0.3px; }
  .product-shot {
    position: absolute; left: 608px; top: 185px; width: 510px; height: 433px;
    border-radius: 12px;
    background: linear-gradient(180deg, var(--product-dark) 0%, var(--product-dark) 14%, var(--product-light) 20%, var(--product-light) 60%, var(--product-fern) 100%);
    opacity: 0.92;
  }
</style>
</head>
<body>
<main class="banner">
  <div class="shelf-top"></div>
  <div class="shelf-front"></div>

  <div class="brand-mark">ANTLER<br>GROVE</div>

  <h1 class="headline">BOUTIQUE<br><span class="accent">PLATYCERIUM</span><br>NURSERY</h1>

  <p class="tagline">Locally propagated and grown<br>in natural shade houses.</p>

  <div class="social">
    <span class="social-dot"></span>
    <p class="social-handle">ANTLER GROVE</p>
  </div>

  <div class="product-shot" role="img" aria-label="Three stubby coolers printed with staghorn fern artwork on a white cracked texture, standing on the shelf behind blurred fern fronds"></div>
</main>
</body>
</html>
```